Business Card for Graphic Design Firm

This project is for a new graphic design firm based in New Jersey called Velmoth. We outsource graphic design and marketing jobs. We want to communicate that this is a professional company but it as well creative and artistic. This card may be used as a horizontal double sided paper card or a vertical single sided translucent card so feel free to submit designs in whichever format or both.
Updates

Reason: Extending the deadline because I'm not exactly satisfied with the designs so far.

Please view the updated project brief

Target Market(s)

Adults aged 25-60

Industry/Entity Type

Graphic Design

Font styles to use
Serif
Sans Serif

Requirements
Nice to have
• Maybe a triangular pattern around the edges similar to our logo

```html
<!DOCTYPE html>
<html lang="en">
<head>
<meta charset="utf-8">
<title>Velmoth Business Card</title>
<link rel="stylesheet" href="https://fonts.googleapis.com/css2?family=Quicksand:wght@400;500;700&display=swap">
<style>
  :root {
    --backdrop: #e4e6e7;
    --paper: #f7f7f5;
    --ink-grey: #6d7b80;
    --teal: #1aa3b5;
    --teal-deep: #0f7f99;
    --sky: #7cc8ec;
    --orange: #f47c20;
    --amber: #fdab1a;
  }
  * { box-sizing: border-box; margin: 0; padding: 0; }
  html, body {
    width: 1200px; height: 873px; overflow: hidden;
    background: var(--backdrop);
    font-family: "Quicksand", sans-serif;
  }
  .sheet {
    width: 1200px; height: 873px;
    display: flex; align-items: center; justify-content: center; gap: 56px;
  }
  .card {
    position: relative;
    width: 520px; height: 300px;
    background: var(--paper);
    box-shadow: 0 2px 6px rgba(0,0,0,.12);
    overflow: hidden;
  }
  .brand {
    display: flex; align-items: center; gap: 10px;
    color: var(--ink-grey); font-weight: 500;
    letter-spacing: .14em; text-transform: uppercase;
  }
  .brand__square { background: var(--orange); flex: none; }

  /* Front: contact side */
  .card--front .brand {
    position: absolute; top: 30px; right: 34px; font-size: 17px;
  }
  .card--front .brand__square { width: 14px; height: 14px; }
  .contact { position: absolute; top: 34px; left: 36px; }
  .contact__name { font-size: 25px; color: var(--teal); font-weight: 400; line-height: 1.2; }
  .contact__name strong { font-weight: 700; }
  .contact__line { font-size: 14px; color: var(--ink-grey); line-height: 1.55; }
  .contact__line--web { color: var(--teal); }
  .contact__lines { margin-top: 8px; }
  .accent-band {
    position: absolute; left: 0; right: 0; bottom: 0; height: 118px;
    background: linear-gradient(100deg, var(--orange) 0%, var(--amber) 38%, var(--sky) 55%, var(--teal) 72%, var(--teal-deep) 100%);
  }

  /* Back: brand side */
  .card--back { display: flex; flex-direction: column; align-items: center; justify-content: center; gap: 14px; }
  .card--back .brand { font-size: 38px; gap: 16px; }
  .card--back .brand__square { width: 26px; height: 26px; }
  .card--back .web { font-size: 16px; color: var(--teal); }
</style>
</head>
<body>
  <main class="sheet">
    <section class="card card--front">
      <div class="brand"><span class="brand__square"></span><span class="brand__name">Velmoth</span></div>
      <div class="contact">
        <p class="contact__name">Dana<strong>Whitfield</strong></p>
        <div class="contact__lines">
          <p class="contact__line">021.478.350</p>
          <p class="contact__line">dana@velmoth.com</p>
          <p class="contact__line contact__line--web">www.velmoth.com</p>
        </div>
      </div>
      <div class="accent-band" role="img" aria-label="Decorative band of orange, amber, sky blue and teal triangles"></div>
    </section>

    <section class="card card--back">
      <div class="brand"><span class="brand__square"></span><span class="brand__name">Velmoth</span></div>
      <p class="web">www.velmoth.com</p>
    </section>
  </main>
</body>
</html>
```